Young and modern Electrical company working in the commercial arena.

Wanting a business card design thats modern and will last. Maybe Minimalist? Happy to look at changing my logo

Target Market(s)

Builders, Project Managers

Industry/Entity Type

Electrical

Contact Information for Business Card

Name
Address
Phone number
Job title

Logo Text

our name or just the logo i'm open to ideas

Font styles to use
Sans Serif

Requirements
Nice to have
• would like to keep the purple in our current logo. it's kinda unique to our market
Should not have
• Don't want it to be to busy. simple is best i think

```html
<!DOCTYPE html>
<html lang="en">
<head>
<meta charset="utf-8">
<title>Halvern Electrical – Business Card</title>
<link href="https://fonts.googleapis.com/css2?family=Montserrat:wght@400;500;600;700&display=swap" rel="stylesheet">
<style>
  :root {
    --backdrop: #3a3b3e;
    --card: #1f1c1e;
    --purple: #6a4bb0;
    --purple-light: #7b5cc4;
    --white: #ffffff;
    --shadow: rgba(0, 0, 0, 0.45);
  }
  * { margin: 0; padding: 0; box-sizing: border-box; }
  html, body { width: 1200px; height: 900px; overflow: hidden; }
  body {
    background: var(--backdrop);
    font-family: "Montserrat", sans-serif;
    color: var(--white);
    position: relative;
  }
  .card {
    position: absolute;
    left: 280px;
    width: 640px;
    height: 366px;
    background: var(--card);
    border-radius: 30px;
    border-bottom: 7px solid var(--purple);
    box-shadow: 0 18px 40px var(--shadow);
    overflow: hidden;
  }
  .card--details { top: 52px; }
  .card--brand { top: 482px; }

  .wordmark {
    font-weight: 700;
    text-transform: uppercase;
    color: var(--white);
    letter-spacing: 0.03em;
    line-height: 1;
    white-space: nowrap;
    display: flex;
    align-items: center;
    gap: 10px;
  }
  .wordmark__dot {
    width: 12px;
    height: 12px;
    border-radius: 50%;
    background: var(--purple-light);
    flex: none;
  }
  .card--details .wordmark {
    position: absolute;
    left: 44px;
    top: 206px;
    font-size: 19px;
  }
  .card--brand .wordmark {
    position: absolute;
    left: 50%;
    top: 50%;
    transform: translate(-50%, -50%);
    font-size: 36px;
    gap: 14px;
  }
  .card--brand .wordmark__dot { width: 18px; height: 18px; }

  .contact {
    position: absolute;
    left: 380px;
    top: 88px;
  }
  .contact__name {
    font-size: 24px;
    font-weight: 600;
    letter-spacing: 0.03em;
    text-transform: uppercase;
    white-space: nowrap;
  }
  .contact__role {
    font-size: 15px;
    font-weight: 500;
    color: var(--purple-light);
    margin-top: 4px;
  }
  .contact__list {
    list-style: none;
    margin-top: 34px;
    font-size: 15px;
    font-weight: 500;
    line-height: 1.35;
  }
  .contact__item {
    display: flex;
    align-items: flex-start;
    gap: 12px;
    margin-bottom: 8px;
  }
  .contact__icon {
    width: 14px;
    height: 14px;
    margin-top: 3px;
    flex: none;
    fill: var(--purple-light);
  }
</style>
</head>
<body>

  <section class="card card--details" aria-label="Business card, contact side">
    <div class="wordmark"><span class="wordmark__dot"></span>Halvern Electrical</div>

    <div class="contact">
      <h1 class="contact__name">Marlo Fenwick</h1>
      <p class="contact__role">CEO | Owner</p>
      <ul class="contact__list">
        <li class="contact__item">
          <svg class="contact__icon" viewBox="0 0 24 24" aria-hidden="true">
            <path d="M6.6 10.8a15.1 15.1 0 0 0 6.6 6.6l2.2-2.2a1 1 0 0 1 1-.25 11.4 11.4 0 0 0 3.6.57 1 1 0 0 1 1 1V20a1 1 0 0 1-1 1A17 17 0 0 1 3 4a1 1 0 0 1 1-1h3.5a1 1 0 0 1 1 1c0 1.25.2 2.460.57 3.6a1 1 0 0 1-.25 1z"/>
          </svg>
          <span>800 555 0192</span>
        </li>
        <li class="contact__item">
          <svg class="contact__icon" viewBox="0 0 24 24" aria-hidden="true">
            <path d="M12 2a7 7 0 0 0-7 7c0 5.25 7 13 7 13s7-7.75 7-13a7 7 0 0 0-7-7zm0 9.5A2.5 2.5 0 1 1 12 6.5a2.5 2.5 0 0 1 0 5z"/>
          </svg>
          <span>418 Larch Street<br>Denver 5678</span>
        </li>
      </ul>
    </div>
  </section>

  <section class="card card--brand" aria-label="Business card, brand side">
    <div class="wordmark"><span class="wordmark__dot"></span>Halvern Electrical</div>
  </section>

</body>
</html>
```